Summer Resolution Do it Now

I run a hypnotherapy practice that helps people
Loose Weight,Stop smoking ,overcome fear of Public speaking and improve Confidence and positive attitude.
I like to market a especific group in the CBD Melbourne as I only practice once a week in the city.

I have some photographs that will go well for the flyer what I am after is something very professional ,sober and elegant.

Target Market(s)

CBD corporate Melbourne market 25 till 60 year old

Industry/Entity Type

Hypnotherapy

Requirements
Must have
• flyer should be two sided , must have http://www.calmtranceclinic.example/ and the phone number 0427916058 and encourage to book online .

```html
<!DOCTYPE html>
<html lang="en">
<head>
<meta charset="utf-8">
<title>Summer Resolution – Hypnotherapy Flyer</title>
<link rel="stylesheet" href="https://fonts.googleapis.com/css2?family=Oswald:wght@300;400;700&family=Roboto+Condensed:wght@300;400;700&display=swap">
<style>
  :root {
    --blue: #0f7cc6;
    --blue-box: #1483cf;
    --orange: #ff6a00;
    --ink: #111111;
    --grey-text: #333333;
    --band: rgba(120,124,138,0.28);
    --page: #e9ecef;
    --white: #ffffff;
    --shirt-green: #2f9c58;
    --shirt-grey: #555b6c;
  }
  * { margin: 0; padding: 0; box-sizing: border-box; }
  html, body { width: 1200px; height: 856px; overflow: hidden; }
  body { background: var(--page); position: relative; font-family: "Roboto Condensed", sans-serif; }

  .flyer { position: absolute; background: var(--white); overflow: hidden; }
  .flyer--front { left: 24px; top: 40px; width: 573px; height: 741px; }
  .flyer--back  { left: 620px; top: 40px; width: 566px; height: 733px; }

  .photo { position: absolute; }
  .flyer--front .photo {
    left: 150px; top: 110px; right: 0; bottom: 0;
    background:
      linear-gradient(to right, #fff 0%, rgba(255,255,255,0.6) 25%, rgba(255,255,255,0) 55%),
      linear-gradient(to bottom, #f3efe4 0%, #ecdcc4 30%, #e2bea4 55%, #d7ae95 70%, #49b36f 85%, var(--shirt-green) 100%);
  }
  .flyer--front .photo-lower {
    position: absolute; left: 110px; top: 640px; right: 0; bottom: 0;
    background: linear-gradient(to right, rgba(47,156,88,0) 0%, rgba(47,156,88,0.85) 18%, var(--shirt-green) 40%);
  }
  .flyer--back .photo {
    left: 250px; top: 0; right: 0; bottom: 0;
    background:
      linear-gradient(to right, #fff 0%, rgba(255,255,255,0) 35%),
      linear-gradient(to bottom, #e8e4e4 0%, #d9b7a3 18%, #cfa591 38%, #7b8092 55%, #5f6679 80%, var(--shirt-grey) 100%);
  }
  .flyer--back .photo-lower {
    position: absolute; left: 110px; top: 592px; right: 0; bottom: 0;
    background: linear-gradient(to right, rgba(85,91,108,0) 0%, rgba(85,91,108,0.9) 12%, var(--shirt-grey) 30%);
  }

  .text { position: absolute; white-space: nowrap; }

  .brand { left: 61px; top: 28px; display: flex; align-items: center; gap: 34px; }
  .brand__dot { width: 99px; height: 99px; border-radius: 50%; background: var(--blue); flex: none; }
  .brand__name { font-family: "Oswald", sans-serif; font-weight: 700; font-size: 30px; line-height: 38px; color: var(--ink); padding-left: 20px; }
  .brand__role { font-family: "Oswald", sans-serif; font-weight: 300; font-size: 29px; line-height: 36px; color: var(--blue); }

  .headline { font-family: "Oswald", sans-serif; font-weight: 700; color: var(--blue); letter-spacing: -0.5px; }
  .cta { font-family: "Oswald", sans-serif; font-weight: 700; color: var(--orange); letter-spacing: -1px; }

  .flyer--front .headline { left: 27px; top: 128px; font-size: 48px; }
  .flyer--front .cta { left: 27px; top: 194px; font-size: 84px; line-height: 100px; }

  .services { position: absolute; list-style: none; }
  .services li { display: flex; align-items: flex-start; gap: 8px; }
  .gear { flex: none; }

  .services--front { left: 28px; top: 320px; font-family: "Oswald", sans-serif; font-weight: 700; font-size: 28px; line-height: 36px; color: var(--ink); }
  .services--front .gear { margin-top: 8px; width: 20px; height: 20px; }

  .book--front { left: 27px; top: 547px; font-family: "Oswald", sans-serif; font-weight: 700; font-size: 22px; line-height: 28px; color: var(--blue); }

  .footer--front { right: 154px; top: 678px; text-align: right; font-family: "Oswald", sans-serif; font-weight: 700; line-height: 24px; }
  .footer--front .address { font-size: 15px; color: var(--ink); }
  .footer--front .web { font-size: 19px; color: var(--white); }

  .flyer--back .headline { left: 26px; top: 26px; font-size: 34px; }
  .flyer--back .cta { left: 26px; top: 62px; font-size: 45px; }
  .intro { left: 26px; top: 126px; font-weight: 300; font-size: 18px; line-height: 22px; color: var(--ink); }
  .book--back { left: 26px; top: 172px; font-family: "Oswald", sans-serif; font-weight: 700; font-size: 23px; line-height: 27px; color: var(--blue); }

  .about {
    position: absolute; left: 0; top: 244px; width: 272px; height: 203px;
    background: var(--blue-box); color: var(--white);
    padding: 8px 12px 0 26px; font-weight: 300; font-size: 12.6px; line-height: 15.5px;
  }

  .services--back { left: 26px; top: 468px; font-weight: 300; font-size: 13.5px; line-height: 16.8px; color: var(--ink); }
  .services--back .gear { margin-top: 3px; width: 12px; height: 12px; }

  .band { position: absolute; left: 0; top: 592px; width: 100%; height: 75px; background: var(--band); }
  .more { left: 27px; top: 604px; font-weight: 300; font-size: 13.5px; line-height: 17px; color: var(--grey-text); }
  .more strong { font-weight: 700; color: var(--ink); }
  .locations { left: 272px; top: 604px; font-weight: 300; font-size: 13.5px; line-height: 18px; color: var(--grey-text); }
  .locations strong { font-weight: 700; color: var(--ink); }
  .badge { position: absolute; left: 476px; top: 598px; width: 66px; height: 66px; border-radius: 50%; background: #f2f2f2; border: 3px solid #7ab648; }
  .web--back { left: 157px; top: 682px; font-family: "Oswald", sans-serif; font-weight: 700; font-size: 19px; color: var(--white); }
</style>
</head>
<body>

<svg width="0" height="0" style="position:absolute" aria-hidden="true">
  <defs>
    <symbol id="gear-icon" viewBox="0 0 20 20">
      <circle cx="10" cy="10" r="7" fill="none" stroke="#0f7cc6" stroke-width="4" stroke-dasharray="3 2.5"/>
      <circle cx="10" cy="10" r="5.5" fill="#0f7cc6"/>
      <circle cx="10" cy="10" r="2.2" fill="#ffffff"/>
    </symbol>
  </defs>
</svg>

<section class="flyer flyer--front">
  <div class="photo" role="img" aria-label="Portrait photo of a smiling blonde woman in a green top"></div>
  <div class="photo-lower" aria-hidden="true"></div>

  <div class="text brand">
    <span class="brand__dot"></span>
    <div>
      <p class="brand__name">Daniel Ashford</p>
      <p class="brand__role">Melbourne Hypnotherapist</p>
    </div>
  </div>

  <h1 class="text headline">Summer Resolution</h1>
  <h2 class="text cta">Do it Now</h2>

  <ul class="services services--front">
    <li><svg class="gear"><use href="#gear-icon"/></svg>Weight Loss program</li>
    <li><svg class="gear"><use href="#gear-icon"/></svg>Stop smoking</li>
    <li><svg class="gear"><use href="#gear-icon"/></svg>Overcome fear of<br>public speaking</li>
    <li><svg class="gear"><use href="#gear-icon"/></svg>Control your anxiety</li>
  </ul>

  <p class="text book--front">Book Online<br>or Call 0427 916 058</p>

  <div class="text footer--front">
    <p class="address">Locations: 42/7 Harbour Ln ,CBD Melbourne</p>
    <p class="web">www.calmtranceclinic.example</p>
  </div>
</section>

<section class="flyer flyer--back">
  <div class="photo" role="img" aria-label="Portrait photo of a smiling dark-haired woman in a grey shirt"></div>
  <div class="photo-lower" aria-hidden="true"></div>

  <h1 class="text headline">Summer Resolution</h1>
  <h2 class="text cta">Do it Now</h2>

  <p class="text intro">Melbourne CBD &amp; Western Suburbs<br>Hypnotherapist Daniel Ashford</p>
  <p class="text book--back">Book Online Below or<br>Call 0427 916 058</p>

  <div class="about">
    Hypnotherapy is a powerful tool and can assist you in making desired changes to your life such as helping you quit smoking, lose weight or to improve public speaking among many other things. Daniel Ashford is a Clinical Hypnotherapist based in Melbourne's CBD and Western Suburbs (Footscray). People from all over Australia come to see Daniel for hypnotherapy consultations. You can book an appointment online to see Daniel via the booking system which can be accessed below. Alternatively,
  </div>

  <ul class="services services--back">
    <li><svg class="gear"><use href="#gear-icon"/></svg>Stopping Smoking</li>
    <li><svg class="gear"><use href="#gear-icon"/></svg>Alcohol Moderation</li>
    <li><svg class="gear"><use href="#gear-icon"/></svg>Losing Weight</li>
    <li><svg class="gear"><use href="#gear-icon"/></svg>Public Speaking Fears</li>
    <li><svg class="gear"><use href="#gear-icon"/></svg>Bruxism / Teeth Grinding /</li>
    <li><svg class="gear"><use href="#gear-icon"/></svg>Teeth Clenching IBS</li>
  </ul>

  <div class="band"></div>
  <p class="text more">And Much More – <strong>Daniel</strong><br>has treated everything from<br>Fear of Flying to Hair Pulling.</p>
  <p class="text locations"><strong>Locations:</strong><br>42/7 Harbour Ln ,CBD Melbourne</p>
  <div class="badge" role="img" aria-label="Professional association membership badge"></div>

  <p class="text web--back">www.calmtranceclinic.example</p>
</section>

</body>
</html>
```